Label for Refill packaging eco-conscious beauty brand

We need a label for our refill pouch. Velvet Harbor is an unscented conditioner formulated using the finest healthy & pure ingredients, free of chemicals and harmful toxins. As a minimalist beauty brand we are proud to be certified with TQB, Norvamark and Silver Kestrel.

We already have the pouches and an exciting label for our regular bottles.
We choose a kraft brown packing for the refill pouch and would like something minimalist but elegant for the label.

```html
<!DOCTYPE html>
<html lang="en">
<head>
<meta charset="utf-8">
<title>Velvet Harbor – Refill Pouch Label</title>
<link rel="stylesheet" href="https://fonts.googleapis.com/css2?family=Marcellus&family=Noto+Sans:wght@400&family=Libre+Baskerville:ital@1&display=swap">
<style>
  :root {
    --kraft: #d6b78c;
    --kraft-light: #ddc098;
    --ink: #1f1a16;
    --rule: #4a3f33;
  }
  html, body {
    margin: 0;
    padding: 0;
    width: 1200px;
    height: 1200px;
    overflow: hidden;
  }
  .label {
    position: relative;
    width: 1200px;
    height: 1200px;
    background: radial-gradient(ellipse at 50% 40%, var(--kraft-light), var(--kraft));
    color: var(--ink);
    text-align: center;
  }
  .brand-name {
    position: absolute;
    top: 410px;
    left: 0;
    right: 0;
    font-family: "Noto Sans", sans-serif;
    font-weight: 400;
    font-size: 58px;
    line-height: 76px;
    letter-spacing: 1px;
  }
  .product-title {
    position: absolute;
    top: 668px;
    left: 0;
    right: 0;
    font-family: "Marcellus", serif;
    font-size: 68px;
    letter-spacing: 1px;
    margin: 0;
    font-weight: 400;
  }
  .rule {
    position: absolute;
    left: 50%;
    transform: translateX(-50%);
    height: 0;
    border-top: 1.5px solid var(--rule);
  }
  .rule--title { top: 757px; width: 580px; }
  .rule--cert-top { top: 882px; width: 620px; }
  .rule--cert-bottom { top: 946px; width: 620px; }
  .product-desc {
    position: absolute;
    top: 768px;
    left: 0;
    right: 0;
    font-family: "Noto Sans", sans-serif;
    font-size: 35px;
    line-height: 40px;
    letter-spacing: 0.5px;
  }
  .certifications {
    position: absolute;
    top: 892px;
    left: 0;
    right: 0;
    font-family: "Libre Baskerville", serif;
    font-style: italic;
    font-size: 27px;
    line-height: 44px;
  }
  .certifications .sep {
    display: inline-block;
    width: 0;
    height: 34px;
    border-left: 1.5px solid var(--rule);
    vertical-align: middle;
    margin: 0 12px;
  }
  .volume {
    position: absolute;
    top: 1078px;
    left: 0;
    right: 0;
    font-family: "Libre Baskerville", serif;
    font-size: 22px;
    letter-spacing: 0.5px;
  }
</style>
</head>
<body>
  <main class="label">
    <div class="brand-name">KLAAR<br>Maren</div>

    <h1 class="product-title">VELVET HARBOR</h1>
    <div class="rule rule--title"></div>

    <p class="product-desc">unscented hair conditioner<br>apres - shampoing non parfum</p>

    <div class="rule rule--cert-top"></div>
    <div class="certifications">TQB Verified<sup>™</sup><span class="sep"></span>Norvamark<span class="sep"></span>Silver Kestrel</div>
    <div class="rule rule--cert-bottom"></div>

    <div class="volume">238ml e / 8fl. oz.</div>
  </main>
</body>
</html>
```